Women's Health Company needs business card

We need a business card for a USA based women's health care company. We use digital technology to enhance therapy prescribed by clinicians for their patients

```html
<!DOCTYPE html>
<html lang="en">
<head>
<meta charset="utf-8">
<title>Lumora Health – Business Cards</title>
<link rel="stylesheet" href="https://fonts.googleapis.com/css2?family=Questrial&display=swap">
<style>
  :root {
    --teal: #74bfbc;
    --purple: #8c559e;
    --white: #ffffff;
    --teal-soft: rgba(116,191,188,0.35);
    --purple-soft: rgba(140,85,158,0.35);
    --backdrop: #3c3c3c;
    --card-shadow: rgba(0,0,0,0.45);
  }
  * { margin: 0; padding: 0; box-sizing: border-box; }
  html, body { width: 1200px; height: 900px; overflow: hidden; }
  body {
    background: var(--backdrop);
    font-family: "Questrial", "Century Gothic", sans-serif;
    position: relative;
  }
  .card {
    position: absolute;
    width: 530px;
    height: 306px;
    overflow: hidden;
    box-shadow: 0 3px 10px var(--card-shadow);
  }
  .card--front-white { left: 54px;  top: 128px; background: var(--white); }
  .card--back-white  { left: 615px; top: 128px; background: var(--white); }
  .card--front-purple{ left: 54px;  top: 465px; background: var(--purple); }
  .card--back-wave   { left: 615px; top: 465px; background: var(--teal); }

  .card__art { position: absolute; inset: 0; width: 530px; height: 306px; }

  .pattern-area {
    position: absolute;
    background: linear-gradient(160deg, var(--teal-soft), var(--purple-soft));
  }
  .card--front-white .pattern-area { left: 392px; top: 14px; width: 138px; height: 278px; }
  .card--back-white .pattern-area  { left: 462px; top: 17px; width: 68px;  height: 276px; }

  .wordmark {
    position: absolute;
    font-weight: 400;
    line-height: 1;
    white-space: nowrap;
    letter-spacing: 0.5px;
  }
  .wordmark--large { font-size: 40px; }
  .wordmark--small { font-size: 26px; }
  .card--front-white .wordmark { left: 78px; top: 134px; color: var(--teal); }
  .card--back-white .wordmark  { left: 38px; top: 46px;  color: var(--teal); }
  .card--front-purple .wordmark{ left: 0; right: 0; text-align: center; top: 133px; color: var(--teal); }
  .card--back-wave .wordmark   { left: 30px; top: 44px;  color: var(--white); }

  .person { position: absolute; }
  .person__name { font-size: 17px; color: var(--teal); letter-spacing: 0.3px; }
  .person__role { font-size: 12px; margin-top: 3px; }
  .card--back-white .person { left: 38px; top: 183px; }
  .card--back-white .person__role { color: var(--purple); }
  .card--back-wave .person { right: 48px; top: 115px; text-align: right; }
  .card--back-wave .person__role { color: var(--white); }

  .contact { position: absolute; list-style: none; font-size: 12px; line-height: 15px; }
  .contact li { display: flex; align-items: center; gap: 6px; }
  .contact svg { width: 11px; height: 11px; flex: none; }
  .card--back-white .contact--lines { left: 38px; top: 237px; color: var(--purple); }
  .card--back-white .contact--place { left: 298px; top: 237px; color: var(--purple); }
  .card--back-wave .contact { right: 48px; text-align: right; color: var(--white); }
  .card--back-wave .contact li { justify-content: flex-end; }
  .card--back-wave .contact--lines { top: 185px; }
  .card--back-wave .contact--place { top: 249px; }
  .contact .web { color: var(--teal); }
  .icon { fill: var(--teal); }
</style>
</head>
<body>

<!-- Front, white -->
<section class="card card--front-white">
  <div class="pattern-area" role="img" aria-label="Decorative pattern of overlapping teal and purple outlined squares"></div>
  <div class="wordmark wordmark--large">Lumora Health</div>
</section>

<!-- Back, white -->
<section class="card card--back-white">
  <div class="pattern-area" role="img" aria-label="Decorative pattern of overlapping teal and purple outlined squares"></div>
  <div class="wordmark wordmark--small">Lumora Health</div>
  <div class="person">
    <div class="person__name">Daniel MARLOW</div>
    <div class="person__role">managing director</div>
  </div>
  <ul class="contact contact--lines">
    <li><svg viewBox="0 0 12 12"><path class="icon" d="M1 5c0-2 2.5-3 5-3s5 1 5 3l-2 .6-.6-1.4H3.6L3 5.6z M3 6h6l1 4H2z"/></svg>555 014 27 90</li>
    <li><svg viewBox="0 0 12 12"><path class="icon" d="M3.5 0h5a1 1 0 0 1 1 1v10a1 1 0 0 1-1 1h-5a1 1 0 0 1-1-1V1a1 1 0 0 1 1-1zm.5 1.5v8h4v-8z"/></svg>888 016 43 21</li>
    <li><svg viewBox="0 0 12 12"><path class="icon" d="M0 2.5h12v1L6 7 0 3.5zM0 5l6 3.5L12 5v5H0z"/></svg>d.marlow@lumorahealth.com</li>
  </ul>
  <ul class="contact contact--place">
    <li>48 Harbor Lane</li>
    <li>Millbrook, New York 12545</li>
    <li class="web">www.lumorahealth.com</li>
  </ul>
</section>

<!-- Front, purple -->
<section class="card card--front-purple">
  <div class="wordmark wordmark--large">Lumora Health</div>
</section>

<!-- Back, teal with wave -->
<section class="card card--back-wave">
  <svg class="card__art" viewBox="0 0 530 306">
    <path d="M0 290 C 110 255 150 150 200 90 C 245 38 400 30 530 90 L530 306 L0 306 Z" fill="var(--white)"/>
    <path d="M0 300 C 120 265 165 160 212 102 C 258 48 405 44 530 99 L530 306 L0 306 Z" fill="var(--purple)"/>
  </svg>
  <div class="wordmark wordmark--small">Lumora Health</div>
  <div class="person">
    <div class="person__name">Daniel MARLOW</div>
    <div class="person__role">managing director</div>
  </div>
  <ul class="contact contact--lines">
    <li>555 014 27 90<svg viewBox="0 0 12 12"><path class="icon" d="M1 5c0-2 2.5-3 5-3s5 1 5 3l-2 .6-.6-1.4H3.6L3 5.6z M3 6h6l1 4H2z"/></svg></li>
    <li>888 016 43 21<svg viewBox="0 0 12 12"><path class="icon" d="M3.5 0h5a1 1 0 0 1 1 1v10a1 1 0 0 1-1 1h-5a1 1 0 0 1-1-1V1a1 1 0 0 1 1-1zm.5 1.5v8h4v-8z"/></svg></li>
    <li>d.marlow@lumorahealth.com<svg viewBox="0 0 12 12"><path class="icon" d="M0 2.5h12v1L6 7 0 3.5zM0 5l6 3.5L12 5v5H0z"/></svg></li>
  </ul>
  <ul class="contact contact--place">
    <li>48 Harbor Lane</li>
    <li>Millbrook, New York 12545</li>
    <li class="web">www.lumorahealth.com</li>
  </ul>
</section>

</body>
</html>
```